Night Guard Packaging

We have designed a sleek night guard for Bruxism (grinding and clenching) and would like a simple design for the front of the box.
We like simple and clean design, so maybe your artist can draw a clean image of the guard instead of using a photo?

Colours:
Our box will be Matt black, similar to example attached.
We are thinking white/black with a hint of green (the same green as the guard, also attached). The “mock-up” box artist design is the one we are leaning towards (the other examples are to give you a feel for what we like). But, if it’s too elegant it won’t feel “medical”.

The logo will need to be inverted, as it is for a white background (original attached)

Words:
Pellora Night Guard (main heading)
For Grinding & Clenching (sun heading below in smaller font).

We like, symmetry, sleek, clean, elegant, luxurious.

Maybe you artist could draw a clean image of the guard instead of using a photo? I screen shot some images with font and artists impressions. But, the customer will need to be able to see/understand the product, from the minimal details on the front of the box, as they won’t be able to open it.

```html
<!DOCTYPE html>
<html lang="en">
<head>
<meta charset="UTF-8">
<title>Pellora Night Guard – Box Front</title>
<link href="https://fonts.googleapis.com/css2?family=Jost:wght@400&display=swap" rel="stylesheet">
<style>
  :root {
    --box-black: #1a1a1a;
    --gold: #9b8a34;
    --gold-light: #a8943a;
  }
  html, body {
    margin: 0;
    padding: 0;
    width: 1200px;
    height: 1200px;
    overflow: hidden;
    background: var(--box-black);
  }
  .box-front {
    position: relative;
    width: 1200px;
    height: 1200px;
    background: var(--box-black);
    font-family: "Jost", "Futura", sans-serif;
    color: var(--gold);
    text-align: center;
  }
  .brand-mark {
    position: absolute;
    top: 250px;
    left: 0;
    right: 0;
    display: flex;
    flex-direction: column;
    align-items: center;
    gap: 18px;
  }
  .brand-mark__circle {
    width: 120px;
    height: 120px;
  }
  .brand-mark__name {
    font-size: 26px;
    font-weight: 400;
    letter-spacing: 0.35em;
    padding-left: 0.35em;
    color: var(--gold-light);
  }
  .product-title {
    position: absolute;
    top: 628px;
    left: 0;
    right: 0;
    margin: 0;
    font-weight: 400;
    line-height: 1;
  }
  .product-title__name {
    display: block;
    font-size: 150px;
    letter-spacing: 0.12em;
    padding-left: 0.12em;
  }
  .product-title__type {
    display: block;
    margin-top: 40px;
    font-size: 76px;
    letter-spacing: 0.14em;
    padding-left: 0.14em;
  }
  .product-tagline {
    position: absolute;
    top: 918px;
    left: 0;
    right: 0;
    margin: 0;
    font-size: 44px;
    font-weight: 400;
    letter-spacing: 0.1em;
    padding-left: 0.1em;
    line-height: 1;
  }
</style>
</head>
<body>
  <main class="box-front">
    <div class="brand-mark">
      <svg class="brand-mark__circle" viewBox="0 0 120 120" aria-hidden="true">
        <circle cx="60" cy="60" r="57" fill="none" stroke="var(--gold)" stroke-width="2"/>
      </svg>
      <div class="brand-mark__name">CORVELLA</div>
    </div>
    <h1 class="product-title">
      <span class="product-title__name">PELLORA</span>
      <span class="product-title__type">NIGHT GUARD</span>
    </h1>
    <p class="product-tagline">FOR GRINDING &amp; CLENCHING</p>
  </main>
</body>
</html>
```